New web page, 2 companies on the one page

A new web page for an engineering consultancy and maintenance management company

Corrick & Associates is the parent company covering the design and consultancy
Trivolt Engineering is the Maintenance and Reliability company

Target Market(s)

Food & Beverage, ingredients Manufacturing
engineering managers

Coding

Coded - Design and coding required

Number of Pages Required

1 page

Font styles to use
Other font styles liked:
• Roboto

Colors
1861ab
85acd3
d0dfed
cee9f5

```html
<!DOCTYPE html>
<html lang="en">
<head>
<meta charset="utf-8">
<title>Trivolt Engineering — Corrick &amp; Associates</title>
<link rel="stylesheet" href="https://fonts.googleapis.com/css2?family=Roboto:wght@400;500;700&family=Montserrat:wght@400;500;600&family=Jost:wght@300;400;500&display=swap">
<style>
:root{
  --blue:#1861ab;
  --blue-dark:#0f4c8f;
  --sky:#85acd3;
  --pale:#d0dfed;
  --ice:#cee9f5;
  --ink:#2b2b2b;
  --grey:#6d6d6d;
  --line:#e4e9f0;
  --foot:#f3f4f6;
  --white:#ffffff;
}
*{margin:0;padding:0;box-sizing:border-box}
html,body{width:1200px;height:3746px;overflow:hidden;background:var(--white)}
body{position:relative;font-family:'Montserrat',sans-serif;color:var(--ink)}
.abs{position:absolute}

/* hero */
.hero{left:0;top:0;width:1200px;height:712px;overflow:hidden}
.hero-photo{position:absolute;inset:0;background:linear-gradient(100deg,#0f1838 0%,#24305c 40%,#5a4a6a 62%,#8a6a70 75%,#2a2f5a 100%)}
.hero-shade{position:absolute;inset:0;background:linear-gradient(90deg,rgba(10,16,40,.75),rgba(10,16,40,.1) 70%)}
.brand{left:119px;top:52px;display:flex;align-items:center;gap:12px;color:var(--white);font-family:'Roboto',sans-serif;font-weight:700;font-size:30px;letter-spacing:1px}
.brand .mark{width:44px;height:44px;border-radius:50%;background:var(--blue)}
.topbar{top:18px;left:858px;color:var(--white);font-family:'Roboto',sans-serif;font-size:14px;display:flex;align-items:center;gap:8px}
.mail{left:1048px;top:18px}
.nav-rule{left:470px;top:57px;width:730px;height:1px;background:rgba(255,255,255,.25)}
.nav{top:73px;left:540px;display:flex;font-family:'Roboto',sans-serif;font-weight:500;font-size:16px;color:var(--white)}
.nav span{padding:0 34px;border-left:1px solid rgba(255,255,255,.3)}
.nav span:first-child{border-left:none;padding-left:26px}
.hero-title{left:180px;top:220px;font-family:'Roboto',sans-serif;font-weight:500;font-size:50px;line-height:58px;color:var(--white);letter-spacing:-.5px}
.btn-hero{left:182px;top:432px;width:170px;height:46px;border-radius:23px;background:var(--blue);color:var(--white);font-family:'Roboto',sans-serif;font-weight:500;font-size:16px;display:flex;align-items:center;justify-content:center}
.arrow-btn{width:42px;height:42px;border-radius:50%;display:flex;align-items:center;justify-content:center}
.arrow-l{left:85px;top:308px;background:rgba(255,255,255,.3)}
.arrow-r{left:1068px;top:308px;background:var(--white)}
.dots{left:519px;top:637px;display:flex;gap:10px}
.dots i{display:block;width:48px;height:4px;background:var(--white)}
.dots i.on{background:var(--blue)}

/* about */
.about-photo{left:126px;top:791px;width:408px;height:408px;border-radius:50%;background:radial-gradient(circle at 40% 40%,#c9d6e6,#4b6385 60%,#1f2f4c)}
.about-ring{left:138px;top:790px;width:408px;height:408px;border-radius:50%;border:2px dotted var(--blue)}
.about h2,.sec-title{font-family:'Montserrat',sans-serif;font-weight:400;font-size:36px;color:#6a6a6a;letter-spacing:-.5px}
.about h2 b,.sec-title b{font-weight:600;color:var(--blue)}
.about{left:630px;top:828px;width:415px}
.about .lead{margin-top:28px;font-size:15px;line-height:26px;color:var(--ink)}
.about p{margin-top:20px;font-size:12.5px;line-height:22px;color:#555}

/* services */
.sec-line{left:599px;top:1267px;width:2px;height:44px;background:#888}
.sec-dot{left:596px;top:1309px;width:8px;height:8px;border-radius:50%;background:#888}
.sec-head{left:0;top:1330px;width:1200px;text-align:center}
.sec-head p{margin-top:10px;font-size:13px;line-height:22px;color:#555}
.grid-rule-h{left:134px;top:1813px;width:938px;height:1px;background:var(--line)}
.grid-rule-v{top:1813px;width:1px;height:330px;background:var(--line)}
.card-hi{left:448px;top:1484px;width:311px;height:328px;background:var(--white);box-shadow:0 6px 30px rgba(24,97,171,.15)}
.svc{width:235px}
.svc svg{display:block}
.svc h3{margin-top:12px;font-weight:500;font-size:17px;line-height:23px;color:var(--ink)}
.svc p{margin-top:14px;font-size:11px;line-height:20px;color:#555}
.svc a{display:block;margin-top:14px;font-size:12px;font-weight:600;color:var(--blue);text-decoration:none}

/* cta */
.cta{left:0;top:2230px;width:1200px;height:522px}
.cta-badge{left:170px;top:2381px;width:234px;height:234px;border-radius:50%;background:var(--blue-dark)}
.cta-text{left:516px;top:2365px;font-family:'Jost',sans-serif;color:var(--white)}
.cta-text .kick{font-weight:300;font-size:34px;color:var(--pale)}
.cta-text h2{margin-top:8px;font-weight:500;font-size:46px;line-height:54px}
.btn-cta{left:519px;top:2570px;width:197px;height:50px;border-radius:25px;background:var(--white);color:var(--blue);font-family:'Jost',sans-serif;font-size:19px;display:flex;align-items:center;justify-content:center}
.cta-photo{left:880px;top:2250px;width:210px;height:500px;background:linear-gradient(180deg,rgba(255,255,255,.06),rgba(10,30,70,.16))}

/* posts */
.post{top:2843px;width:287px;height:382px;background:var(--white);box-shadow:0 4px 22px rgba(0,0,0,.1)}
.post .img{height:175px}
.post .body{padding:20px 24px}
.post .by{font-size:12px;color:#777;font-family:'Jost',sans-serif}
.post h4{margin-top:6px;font-family:'Jost',sans-serif;font-weight:400;font-size:19px;line-height:23px;color:var(--ink)}
.post p{margin-top:8px;font-family:'Jost',sans-serif;font-size:14px;line-height:19px;color:#666}
.post a{display:block;margin-top:10px;font-family:'Jost',sans-serif;font-size:14px;color:var(--blue)}

/* footer */
.footer{left:0;top:3310px;width:1200px;height:436px}
.foot-brand{left:180px;top:3444px;display:flex;align-items:center;gap:12px;font-family:'Roboto',sans-serif;font-weight:700;font-size:28px;color:var(--ink)}
.foot-brand .mark{width:50px;height:50px;border-radius:50%;background:var(--blue)}
.foot-addr{left:202px;top:3531px;font-family:'Jost',sans-serif;font-size:15px;line-height:19px;color:#444}
.foot-phone{left:202px;top:3600px;font-family:'Jost',sans-serif;font-size:18px;color:var(--blue)}
.foot h5{font-family:'Roboto',sans-serif;font-weight:500;font-size:18px;color:var(--ink)}
.links{left:516px;top:3436px}
.links ul{list-style:none;margin-top:14px}
.links li{font-family:'Jost',sans-serif;font-size:14px;line-height:30.5px;color:#333}
.links li::before{content:"›";margin-right:8px;font-size:16px}
.sub{left:708px;top:3436px}
.field{left:701px;top:3482px;width:327px;height:38px;border:1px solid #bbb;border-radius:19px;background:var(--white)}
.field span{position:absolute;left:22px;top:10px;font-family:'Jost',sans-serif;font-size:14px;color:#777}
.field b{position:absolute;right:-1px;top:-1px;width:113px;height:38px;border-radius:0 19px 19px 0;background:var(--blue);color:var(--white);font-family:'Jost',sans-serif;font-weight:400;font-size:17px;display:flex;align-items:center;justify-content:center}
.follow{left:708px;top:3546px}
.social{top:3580px;width:36px;height:36px;border-radius:50%;background:var(--blue)}
.foot-rule{left:0;top:3673px;width:1200px;height:1px;background:#d5d8dd}
.copy{top:3698px;font-family:'Roboto',sans-serif;font-size:13px;color:#444}
</style>
</head>
<body>

<!-- HERO -->
<section class="hero abs">
  <div class="hero-photo" role="img" aria-label="Hand stacking wooden blocks under a glowing network of engineering icons"></div>
  <div class="hero-shade"></div>
</section>
<svg class="abs" style="left:0;top:600px" width="1200" height="112" viewBox="0 0 1200 112">
  <polygon points="0,20 600,96 1200,20 1200,112 0,112" fill="#fff"/>
  <polyline points="0,20 600,96" fill="none" stroke="#6a6e78" stroke-width="7"/>
  <polyline points="600,96 1200,20" fill="none" stroke="var(--blue)" stroke-width="7"/>
</svg>

<div class="brand abs"><span class="mark"></span>TRIVOLT</div>
<div class="topbar abs">
  <svg width="16" height="16" viewBox="0 0 24 24"><path d="M6 2l4 4-2 3a11 11 0 007 7l3-2 4 4-3 4C10 22 2 14 2 5z" fill="none" stroke="#fff" stroke-width="1.8"/></svg>
  (555) 014-2290
</div>
<svg class="mail abs" width="22" height="16" viewBox="0 0 22 16"><rect x="1" y="1" width="20" height="14" fill="none" stroke="#fff" stroke-width="1.5"/><polyline points="1,1 11,9 21,1" fill="none" stroke="#fff" stroke-width="1.5"/></svg>
<div class="nav-rule abs"></div>
<nav class="nav abs"><span>HOME</span><span>ABOUT US</span><span>SERVICES ▾</span><span>CONTACT US</span></nav>

<h1 class="hero-title abs">Engineering<br>Maintenance &amp;<br>Reliability company</h1>
<div class="btn-hero abs">WHO WE ARE</div>
<div class="arrow-btn arrow-l abs"><svg width="14" height="14" viewBox="0 0 14 14"><polyline points="9,2 4,7 9,12" fill="none" stroke="#fff" stroke-width="2"/></svg></div>
<div class="arrow-btn arrow-r abs"><svg width="14" height="14" viewBox="0 0 14 14"><polyline points="5,2 10,7 5,12" fill="none" stroke="var(--blue)" stroke-width="2"/></svg></div>
<div class="dots abs"><i></i><i class="on"></i><i></i></div>

<!-- ABOUT -->
<svg class="abs" style="left:0;top:700px" width="340" height="460" viewBox="0 0 340 460"><path d="M250,0 C330,80 360,200 300,320 C240,420 100,460 0,450" fill="none" stroke="#aaa" stroke-dasharray="2 4"/></svg>
<div class="about-photo abs" role="img" aria-label="Two engineers in suits reviewing a tablet together"></div>
<div class="about-ring abs"></div>
<div class="about abs">
  <h2>ABOUT <b>TRIVOLT</b></h2>
  <div class="lead">Corrick &amp; Associates is specialised manufacturing engineering support organisation that can provide fast, nimble, and flexible services.</div>
  <p>We have a proven track record in delivering tangible outcomes in process design and fit-out, project management, manufacturing process and maintenance design and execution.</p>
  <p>Our specialist focus in food manufacturing across a range of sectors allows our team to deliver real benefits to performance and recognition of the clients investment.</p>
</div>

<!-- SERVICES -->
<div class="sec-line abs"></div><div class="sec-dot abs"></div>
<div class="sec-head abs">
  <h2 class="sec-title">OUR <b>SERVICES</b></h2>
  <p>Our specialist focus in food manufacturing across a range of sectors<br>allows our team to deliver real benefits to performance.</p>
</div>
<div class="card-hi abs"></div>
<div class="grid-rule-h abs"></div>
<div class="grid-rule-v abs" style="left:447px"></div>
<div class="grid-rule-v abs" style="left:760px"></div>

<div class="svc abs" style="left:175px;top:1534px">
  <svg width="52" height="52" viewBox="0 0 52 52"><rect x="2" y="8" width="30" height="40" rx="4" fill="#e8ecf1"/><circle cx="20" cy="12" r="4" fill="none" stroke="#123" stroke-width="2"/><circle cx="20" cy="40" r="4" fill="none" stroke="#123" stroke-width="2"/><path d="M24 12h16v14H12v10" fill="none" stroke="var(--blue)" stroke-width="2"/></svg>
  <h3>Process &amp;<br>Facilities Design</h3>
  <p>Lorem Ipsum is simply dummy text of the printing and typesetting industry. Lorem Ipsum has been.</p>
  <a>Learn More &nbsp;→</a>
</div>
<div class="svc abs" style="left:488px;top:1534px">
  <svg width="52" height="52" viewBox="0 0 52 52"><rect x="2" y="8" width="30" height="40" rx="4" fill="#e8ecf1"/><circle cx="22" cy="22" r="10" fill="none" stroke="#123" stroke-width="2" stroke-dasharray="4 2"/><circle cx="22" cy="22" r="4" fill="none" stroke="#123" stroke-width="2"/><circle cx="38" cy="38" r="7" fill="none" stroke="var(--blue)" stroke-width="2"/></svg>
  <h3>Project<br>Management</h3>
  <p>Lorem Ipsum is simply dummy text of the printing and typesetting industry. Lorem Ipsum has been.</p>
  <a>Learn More &nbsp;→</a>
</div>
<div class="svc abs" style="left:800px;top:1534px">
  <svg width="60" height="52" viewBox="0 0 60 52"><rect x="2" y="8" width="30" height="40" rx="4" fill="#e8ecf1"/><rect x="12" y="4" width="44" height="30" rx="2" fill="none" stroke="#123" stroke-width="2"/><circle cx="26" cy="19" r="5" fill="none" stroke="var(--blue)" stroke-width="2"/><circle cx="42" cy="19" r="5" fill="none" stroke="var(--blue)" stroke-width="2"/><line x1="28" y1="40" x2="40" y2="40" stroke="#123" stroke-width="2"/></svg>
  <h3>Major Equipment &amp;<br>Services Installation</h3>
  <p>Lorem Ipsum is simply dummy text of the printing and typesetting industry. Lorem Ipsum has been.</p>
  <a>Learn More &nbsp;→</a>
</div>
<div class="svc abs" style="left:175px;top:1866px">
  <svg width="52" height="52" viewBox="0 0 52 52"><rect x="2" y="8" width="30" height="40" rx="4" fill="#e8ecf1"/><circle cx="22" cy="16" r="8" fill="none" stroke="#123" stroke-width="2" stroke-dasharray="4 2"/><circle cx="34" cy="34" r="9" fill="none" stroke="var(--blue)" stroke-width="2" stroke-dasharray="4 2"/><circle cx="34" cy="34" r="3" fill="none" stroke="#123" stroke-width="2"/></svg>
  <h3>Engineering and<br>Maintenance</h3>
  <p>Lorem Ipsum is simply dummy text of the printing and typesetting industry. Lorem Ipsum has been.</p>
  <a>Learn More &nbsp;→</a>
</div>
<div class="svc abs" style="left:487px;top:1866px">
  <svg width="52" height="52" viewBox="0 0 52 52"><rect x="2" y="8" width="30" height="40" rx="4" fill="#e8ecf1"/><circle cx="28" cy="22" r="13" fill="none" stroke="#123" stroke-width="2" stroke-dasharray="5 2"/><circle cx="28" cy="22" r="6" fill="none" stroke="var(--blue)" stroke-width="2"/><path d="M14 44h18" stroke="#123" stroke-width="2"/></svg>
  <h3>Maintenance<br>Execution</h3>
  <p>Lorem Ipsum is simply dummy text of the printing and typesetting industry. Lorem Ipsum has been.</p>
  <a>Learn More &nbsp;→</a>
</div>
<div class="svc abs" style="left:800px;top:1866px">
  <svg width="52" height="52" viewBox="0 0 52 52"><rect x="2" y="8" width="30" height="40" rx="4" fill="#e8ecf1"/><rect x="10" y="6" width="26" height="36" rx="2" fill="none" stroke="#123" stroke-width="2"/><line x1="16" y1="16" x2="30" y2="16" stroke="#123" stroke-width="2"/><line x1="16" y1="24" x2="26" y2="24" stroke="#123" stroke-width="2"/><circle cx="36" cy="36" r="7" fill="none" stroke="var(--blue)" stroke-width="2"/><line x1="41" y1="41" x2="48" y2="48" stroke="var(--blue)" stroke-width="2.5"/></svg>
  <h3>Vision Inspection<br>Systems</h3>
  <p>Lorem Ipsum is simply dummy text of the printing and typesetting industry. Lorem Ipsum has been.</p>
  <a>Learn More &nbsp;→</a>
</div>

<!-- CTA -->
<svg class="cta abs" width="1200" height="522" viewBox="0 0 1200 522">
  <polygon points="0,72 600,3 1200,72 1200,522 0,522" fill="var(--blue)"/>
</svg>
<div class="cta-badge abs"></div>
<div class="cta-photo abs" role="img" aria-label="Photo of a smiling woman holding a phone"></div>
<div class="cta-text abs">
  <div class="kick">Change starts here</div>
  <h2>Take your first step<br>towards RESULT.</h2>
</div>
<div class="btn-cta abs">Email us Today</div>

<!-- POSTS -->
<article class="post abs" style="left:132px">
  <div class="img" role="img" aria-label="Hands reviewing financial charts on a desk" style="background:linear-gradient(135deg,#d9dee6,#6c7a92 60%,#2c3750)"></div>
  <div class="body"><div class="by">By Admin</div><h4>Lorem Ipsum is simply dummy text of the printing</h4><p>There are many variations of passages of available but majority have alteration</p><a><u>Read More</u></a></div>
</article>
<article class="post abs" style="left:457px">
  <div class="img" role="img" aria-label="Hands holding glowing gears over a digital interface" style="background:linear-gradient(135deg,#9fc2e4,#3d6ea6 55%,#1b2e52)"></div>
  <div class="body"><div class="by">By Admin</div><h4>Lorem Ipsum is simply dummy text of the printing</h4><p>There are many variations of passages of available but majority have alteration</p><a><u>Read More</u></a></div>
</article>
<article class="post abs" style="left:781px">
  <div class="img" role="img" aria-label="Team of colleagues reviewing documents at a table" style="background:linear-gradient(135deg,#eef0f2,#a9a7a6 55%,#4d4a50)"></div>
  <div class="body"><div class="by">By Admin</div><h4>Lorem Ipsum is simply dummy text of the printing</h4><p>There are many variations of passages of available but majority have alteration</p><a><u>Read More</u></a></div>
</article>

<!-- FOOTER -->
<svg class="footer abs" width="1200" height="436" viewBox="0 0 1200 436">
  <polygon points="0,50 600,0 1200,50 1200,436 0,436" fill="var(--foot)"/>
</svg>
<div class="foot-brand abs"><span class="mark"></span>CORRICK</div>
<svg class="abs" style="left:176px;top:3532px" width="16" height="20" viewBox="0 0 16 20"><path d="M8 1a6 6 0 016 6c0 5-6 12-6 12S2 12 2 7a6 6 0 016-6z" fill="none" stroke="#333" stroke-width="1.8"/><circle cx="8" cy="7" r="2" fill="#333"/></svg>
<div class="foot-addr abs">Corrick Associates<br>418 Harlow Lane<br>Brookfield, WI 53005</div>
<svg class="abs" style="left:175px;top:3603px" width="18" height="18" viewBox="0 0 24 24"><path d="M6 2l4 4-2 3a11 11 0 007 7l3-2 4 4-3 4C10 22 2 14 2 5z" fill="#333"/></svg>
<div class="foot-phone abs">(555) 018-3374</div>

<div class="foot links abs"><h5>COMPANY</h5><ul><li>Home</li><li>About Us</li><li>Services</li><li>Sitemap</li><li>Contact Us</li></ul></div>
<div class="foot sub abs"><h5>SUBSCRIBE</h5></div>
<div class="field abs"><span>Email address</span><b>Subscribe</b></div>
<div class="foot follow abs"><h5>FOLLOW US</h5></div>
<div class="social abs" style="left:709px"></div>
<div class="social abs" style="left:760px"></div>
<div class="social abs" style="left:812px"></div>

<div class="foot-rule abs"></div>
<div class="copy abs" style="left:178px">© 2021 Corrick Associates. All Rights Reserved.</div>
<div class="copy abs" style="left:916px">Privacy Policy &nbsp;|&nbsp; Terms of Use</div>

</body>
</html>
```